Business is backhoe and truck hire. As the title indicates, we dig dirt. Colours preferred are charcoal, red and or orange. Would like a backhoe on the card,possibly a designs with the silhouette of the machine in the background. I We would like to incorporate a large tick in the title for solutions. I thought it could be part of the "W" . Our shirts are Black polo's with orange lines around sleeves and sides. We are a new business in rural Qld, happy to do the smaller jobs that others wont.

Industry/Entity Type

Business

Contact Information for Business Card

Tall Creek Groundworks Solutions

Backhoe and Truck Hire
ABN:58214096371

Peter Kellow
PH: 0491 736 204
PH: 0491 862 035
PH: 4283 6147 a/h

email: tcgsolutions@mailbox-example.com

```html
<!DOCTYPE html>
<html lang="en">
<head>
<meta charset="utf-8">
<title>Tall Creek Groundworks Solutions – Business Card</title>
<link rel="stylesheet" href="https://fonts.googleapis.com/css2?family=Open+Sans:wght@400;600;700&display=swap">
<style>
  :root {
    --page: #eceded;
    --orange: #ee7322;
    --charcoal: #2e2d2d;
    --charcoal-deep: #1c1c1c;
    --title-ink: #2b2a29;
    --white: #ffffff;
    --gravel-dark: #111111;
    --gravel-mid: #3a3a3a;
    --machine-yellow: #d9c52a;
  }
  * { box-sizing: border-box; margin: 0; padding: 0; }
  html, body {
    width: 1200px; height: 806px; overflow: hidden;
    background: var(--page);
    font-family: "Open Sans", Arial, sans-serif;
  }
  .card {
    position: absolute; left: 40px; top: 62px;
    width: 1120px; height: 682px;
    background: var(--charcoal);
    overflow: hidden;
  }
  .card__band {
    position: absolute; left: 0; top: 0; width: 100%; height: 185px;
    background: var(--orange);
    display: flex; align-items: center; justify-content: center;
  }
  .card__company {
    font-weight: 700; font-size: 52px; color: var(--title-ink);
    letter-spacing: 0.2px; padding-top: 18px;
  }
  .card__gravel {
    position: absolute; left: 0; bottom: 0; width: 100%; height: 175px;
    background: linear-gradient(180deg, rgba(0,0,0,0) 0%, var(--gravel-mid) 30%, var(--gravel-dark) 100%);
  }
  .card__machine {
    position: absolute; left: 620px; top: 285px; width: 490px; height: 340px;
    border-radius: 18px;
    background: radial-gradient(ellipse at 45% 50%, var(--machine-yellow) 0%, #6b6420 45%, rgba(30,30,30,0) 75%);
  }
  .card__service {
    position: absolute; left: 0; width: 1195px; top: 220px;
    text-align: center; color: var(--white);
    font-weight: 600; font-size: 40px;
  }
  .card__abn {
    position: absolute; right: 283px; top: 283px;
    color: var(--white); font-size: 24px;
  }
  .contact {
    position: absolute; left: 163px; top: 345px; color: var(--white);
  }
  .contact__name {
    color: var(--orange); font-weight: 600; font-size: 36px; margin-bottom: 22px;
  }
  .contact__line { font-size: 31px; line-height: 42.5px; }
  .contact__email { font-size: 30px; }
  .icon { position: absolute; }
  .icon--phone { left: 118px; top: 462px; }
  .icon--mail { left: 112px; top: 552px; }
</style>
</head>
<body>
  <div class="card">
    <div class="card__gravel" role="img" aria-label="Dark gravel and soil texture along the bottom of the card"></div>
    <div class="card__machine" role="img" aria-label="Photograph of a yellow backhoe loader"></div>

    <header class="card__band">
      <h1 class="card__company">Tall Creek Groundworks Solutions</h1>
    </header>

    <p class="card__service">Backhoe and Truck Hire</p>
    <p class="card__abn">ABN:58214096371</p>

    <svg class="icon icon--phone" width="26" height="32" viewBox="0 0 26 32" aria-hidden="true">
      <path d="M7 2 L11 9 L8 12 Q10 19 15 23 L18 20 L24 25 L20 30 Q9 28 3 14 Q2 6 7 2 Z" fill="none" stroke="var(--orange)" stroke-width="3" stroke-linejoin="round"/>
    </svg>
    <svg class="icon icon--mail" width="38" height="26" viewBox="0 0 38 26" aria-hidden="true">
      <rect x="2" y="2" width="34" height="22" fill="none" stroke="var(--orange)" stroke-width="2.5"/>
      <path d="M2 2 L19 15 L36 2" fill="none" stroke="var(--orange)" stroke-width="2.5"/>
    </svg>

    <div class="contact">
      <p class="contact__name">Peter Kellow</p>
      <p class="contact__line">0491 736 204</p>
      <p class="contact__line">0491 862 035</p>
      <p class="contact__line">4283 6147</p>
      <p class="contact__line contact__email">tcgsolutions@mailbox-example.com</p>
    </div>
  </div>
</body>
</html>
```